starlitmanesandtails pet therapy animals

I would like a business card to genarate posative emotions within people. My program has been running in a retirement village for over 5 years I work with residents and family members. My dogs work in palative care and are a great support to family members at the end stage. I also support the families and friends at furnerals when needed to dogs are always with me. Starlitmanes started with the death of my first therapy dog Milo there was such an out cry of grief within the town and retirement village that he had his own furneral The hooves came into it when I was donated a beautiful Miniature horse for the pet therapy program with great results. I now need something very special as a business card. Eg Angelwings my dogs are King Charles Cavaliers so with what I have described can you create something beautiful to acknowledge to work I do and promote it more.

Reason: The reason I have extended the deadline to give other designers a chance to look at the job. So far I have 3 designs. I am hoping to get a few more.

Industry/Entity Type

Town

Contact Information for Business Card

Starlitmanesandtails pet therapy animals
Rosalind Varga
E-mail starlitmanesandtails@quellnet.com
Mobile 0417650382
Pet therapy animals give unconditional love to the aged and disabled.

Font styles to use
Decorative

Colors

Designer to choose colors to be used in the design.

Requirements
Nice to have
• angelwings a King Charles Cavalier tan and white with angel wings and a horse with angel wings

```html
<!DOCTYPE html>
<html lang="en">
<head>
<meta charset="utf-8">
<title>Starlit Manes and Tails — Business Card</title>
<link rel="stylesheet" href="https://fonts.googleapis.com/css2?family=Quicksand:wght@300;400&family=Rye&display=swap">
<style>
  :root {
    --page: #ece9e1;
    --card: #d7cf8c;
    --cream: #f3efdf;
    --ink: #6a4a22;
    --ink-soft: #8a7444;
    --coat-tan: #b56a34;
    --coat-white: #f4eee2;
  }
  * { box-sizing: border-box; margin: 0; padding: 0; }
  html, body { width: 1200px; height: 918px; overflow: hidden; background: var(--page); }
  .canvas { position: relative; width: 1200px; height: 918px; }

  .card {
    position: absolute;
    left: 250px;
    width: 700px;
    height: 400px;
    background: var(--card);
    box-shadow: 0 6px 18px rgba(60, 45, 20, 0.18);
    overflow: hidden;
  }
  .card--back { top: 39px; }
  .card--front { top: 479px; }
  .card__bands { position: absolute; inset: 0; }

  /* back */
  .brand-mark {
    position: absolute;
    left: 0; right: 0; top: 120px;
    display: flex; align-items: center; justify-content: center; gap: 14px;
    font-family: "Quicksand", sans-serif;
    font-weight: 400;
    font-size: 34px;
    color: var(--cream);
  }
  .brand-mark__dot {
    width: 26px; height: 26px; border-radius: 50%;
    background: var(--cream);
  }
  .tagline {
    position: absolute;
    left: 0; right: 0; top: 250px;
    text-align: center;
    font-family: "Quicksand", sans-serif;
    font-weight: 300;
    font-size: 18px;
    color: var(--ink-soft);
  }

  /* front */
  .art { position: absolute; }
  .art--pegasus { left: 24px; top: 16px; width: 66px; height: 56px; background: var(--card); opacity: .55; border-radius: 8px; }
  .art--wings { left: 28px; top: 108px; width: 92px; height: 44px; background: var(--cream); opacity: .75; border-radius: 22px; }
  .art--dog {
    left: 66px; top: 236px; width: 160px; height: 136px; border-radius: 46%;
    background: radial-gradient(ellipse at 50% 40%, var(--coat-tan) 0 30%, #d9a77a 55%, var(--coat-white) 80%);
    opacity: .95;
  }
  .art--paw { left: 618px; top: 338px; width: 44px; height: 40px; background: var(--card); border-radius: 50%; opacity: .9; }

  .title {
    position: absolute;
    right: 40px; top: 128px;
    font-family: "Rye", serif;
    font-weight: 400;
    font-size: 26px;
    letter-spacing: 2px;
    text-transform: uppercase;
    color: var(--ink);
    white-space: nowrap;
  }
  .subtitle {
    position: absolute;
    right: 110px; top: 172px;
    font-family: "Quicksand", sans-serif;
    font-weight: 400;
    font-size: 20px;
    color: var(--ink);
  }
  .contact {
    position: absolute;
    left: 300px; top: 210px;
    font-family: "Quicksand", sans-serif;
    font-weight: 400;
    font-size: 19px;
    line-height: 29px;
    color: var(--ink);
    list-style: none;
  }
</style>
</head>
<body>
<main class="canvas">

  <section class="card card--back" aria-label="Card back">
    <div class="brand-mark"><span class="brand-mark__dot"></span><span>Starlit Manes and Tails</span></div>
    <p class="tagline">“ Pet therapy animals give unconditional love to the aged and disabled. ”</p>
  </section>

  <section class="card card--front" aria-label="Card front">
    <svg class="card__bands" width="700" height="400" viewBox="0 0 700 400" aria-hidden="true">
      <path d="M0,0 H700 V215 C690,150 640,115 540,105 C400,92 200,90 0,88 Z" fill="var(--cream)"/>
      <path d="M0,260 C40,320 120,352 260,362 C420,372 560,372 700,362 V400 H0 Z" fill="var(--cream)"/>
    </svg>

    <div class="art art--pegasus" role="img" aria-label="Small winged horse silhouette"></div>
    <div class="art art--wings" role="img" aria-label="Small pair of angel wings"></div>
    <div class="art art--dog" role="img" aria-label="Photo of a tan and white Cavalier King Charles spaniel with angel wings"></div>
    <div class="art art--paw" role="img" aria-label="Paw print icon"></div>

    <h1 class="title">Starlit Manes and Tails</h1>
    <p class="subtitle">pet therapy animals</p>
    <ul class="contact">
      <li>Rosalind Varga</li>
      <li>Email: starlitmanesandtails@quellnet.com</li>
      <li>Contact: 0417650382</li>
    </ul>
  </section>

</main>
</body>
</html>
```